Worldwide Forum on Tension Molecules

We are arranging a meeting in Finland in August: THE 8th WORLDWIDE FORUM ON TENSION MOLECULES IN LIFE AND HEALING - TENSION HANDLING ROUTES AND CIRCUITS.

The program and speakers are included in the Word files. The basic poster arrangement could be a little bit like in the Conference:
http://events.qarvu.net/files/posters/1483956274_17-modulators-ferns.pdf

Basically only the organizers and invited speakers will be listed.

We would like to have some summery maritime background of the kind provided in the stock footage. In addition, we would include some summer views from the City of Turku. We have added a few potential University Campus views in the footage folder.
Updates

Project Deadline Extended
Reason: There was one design that was attractive. We wanted to extend the time available to work along the approach of this design.

Target Market(s)

Scientists in the field of cell stress research

Industry/Entity Type

Management

Requirements
Must have
• There must be the logo of our home university:
• https://www.veltrin.fi/personal/media/3991/vtenglogobasic4c.jpg
• ...somewhere down on the poster, a little bit like QARV in the example above.
• There must also be the logo of the organizing organization Tissue Strain Global Union:
• http://www.tissuestrainreplies.org/?
• All text should be readable (no light text on light background and vice versa)

```html
<!DOCTYPE html>
<html lang="en">
<head>
<meta charset="utf-8">
<title>TSGU Forum 2017 — Tension Handling Routes and Circuits</title>
<link rel="stylesheet" href="https://fonts.googleapis.com/css2?family=Open+Sans:wght@400;600;700;800&family=Playfair+Display:ital,wght@1,500;1,700&display=swap">
<style>
:root{
  --sky:#9fb1b8;
  --sea:#1f6f83;
  --paper:#e8eaeb;
  --teal:#3a9a92;
  --teal-dark:#2d7f79;
  --ink:#2f3335;
  --white:#ffffff;
}
*{margin:0;padding:0;box-sizing:border-box}
html,body{width:848px;height:1200px;overflow:hidden;background:var(--paper)}
body{font-family:"Open Sans",Arial,sans-serif;color:var(--ink)}
.poster{position:relative;width:848px;height:1200px;overflow:hidden;background:var(--paper)}
.abs{position:absolute}

.hero-photo{left:0;top:0;width:848px;height:560px;
  background:linear-gradient(180deg,var(--sky) 0%,#b2c1c6 32%,#4f6f78 40%,var(--sea) 46%,#1c6a80 62%,#2b7c8f 80%,rgba(232,234,235,1) 100%)}
.society-mark{left:162px;top:22px;width:126px;height:126px;border-radius:50%;background:var(--teal-dark)}
.society-name{left:28px;top:168px;font-size:28px;font-weight:700;color:#111;letter-spacing:-.6px;line-height:34px;white-space:nowrap}
.society-tag{left:30px;top:201px;font-size:9px;font-weight:600;color:#111;line-height:11px}
.event-title{left:36px;top:312px;color:var(--white);font-family:"Playfair Display",serif;font-style:italic}
.event-title .small{display:block;font-size:40px;font-weight:500;letter-spacing:1px;line-height:44px}
.event-title .year{display:block;font-size:150px;font-weight:700;line-height:120px;margin-top:-2px}

.watermark{left:232px;top:550px;width:380px;height:380px;border-radius:50%;border:14px solid rgba(200,120,110,.08)}

.col-head{font-size:14px;font-weight:700;color:var(--teal);padding-bottom:3px;border-bottom:2px solid var(--teal);line-height:18px}
.keynotes{left:28px;top:540px;width:230px}
.invited{left:287px;top:540px;width:250px}
.list{list-style:none;font-size:11px;line-height:14.5px;color:var(--ink);margin-top:19px}
.invited-b{left:588px;top:578px;margin-top:0}
.divider{width:1px;background:#b8bcbe;top:562px;height:190px}

.banner-line{left:0;top:798px;width:848px;height:3px;background:var(--teal)}
.forum-name{left:52px;top:768px;font-size:16px;font-weight:700;line-height:17px;color:var(--ink);background:var(--paper);padding-right:10px}
.tag{top:772px;height:32px;background:var(--teal);color:var(--white);font-size:11px;font-weight:600;line-height:13px;padding:3px 16px;transform:skewX(-18deg)}
.tag span{display:block;transform:skewX(18deg)}
.tag-a{left:552px;width:134px}
.tag-b{left:702px;width:160px;padding-left:30px}
.theme{left:0;width:848px;top:814px;text-align:center;font-size:26px;font-weight:700;color:var(--teal);letter-spacing:-.3px;line-height:32px}
.dates{left:0;width:848px;top:843px;text-align:center;font-size:25px;font-weight:700;color:var(--ink);line-height:30px}

.info h3{font-size:13px;font-weight:700;color:var(--teal);line-height:16px}
.info p{font-size:11px;line-height:14.5px}
.venue{left:28px;top:885px}
.organizer{left:28px;top:945px}
.coorg{left:287px;top:885px}
.coorg2{left:287px;top:960px}
.partner{left:583px;top:885px}
.union{left:583px;top:960px}

.footer-line{left:0;top:1028px;width:848px;height:3px;background:var(--teal)}
.footer-photo{left:0;top:1034px;width:848px;height:166px;
  background:linear-gradient(180deg,#3e9896 0%,#2c8586 45%,#1e6d72 100%)}
.contact-box{left:210px;top:1040px;width:360px;height:38px;background:var(--teal-dark);color:var(--white);font-size:27px;font-weight:700;text-align:center;line-height:38px}
.contact{left:0;width:848px;text-align:center;color:var(--white);font-weight:700}
.contact-1{top:1079px;font-size:12px;line-height:15px}
.contact-2{top:1094px;font-size:9px;line-height:11px}
.contact-3{top:1116px;font-size:11px;line-height:15px}
.contact-4{top:1162px;font-size:10.5px;font-weight:600;line-height:14px}
.uni-mark{left:710px;top:1052px;width:56px;height:56px;border-radius:50%;background:rgba(255,255,255,.9)}
.uni-name{left:670px;top:1140px;width:130px;text-align:center;color:var(--white);font-size:17px;font-weight:700;line-height:19px}
</style>
</head>
<body>
<main class="poster">
  <div class="abs hero-photo" role="img" aria-label="Summer sea view with a wooded island shoreline and a distant sailboat under a grey sky"></div>
  <div class="abs society-mark" aria-hidden="true"></div>
  <div class="abs society-name">Tissue Strain Global Union</div>
  <div class="abs society-tag">Publishers of Strain &amp; Fold Letters</div>
  <h1 class="abs event-title"><span class="small">TSGU FORUM</span><span class="year">2017</span></h1>

  <div class="abs watermark" aria-hidden="true"></div>

  <section class="abs keynotes">
    <h2 class="col-head">Keynotes (35 min + 10 min)</h2>
    <ol class="list">
      <li>1. Anne Marchetti, UK</li>
      <li>2. Marja Lehtola, Denmark</li>
      <li>3. Rick Tanabe, USA</li>
      <li>4. Peter Wendel, USA</li>
    </ol>
  </section>
  <div class="abs divider" style="left:258px"></div>
  <section class="abs invited">
    <h2 class="col-head">Invited speakers (20 min + 10 min)</h2>
    <ol class="list">
      <li>1. Cristina Baldarin, Brazil</li>
      <li>2. Rochelle Bernstahl, USA</li>
      <li>3. Stuart Caldmoor, USA</li>
      <li>4. Serena Corti, Italy</li>
      <li>5. Ehud Levran, Israel</li>
      <li>6. Antonio De Luca, USA</li>
      <li>7. Albena Petrova-Ilieva, UK</li>
      <li>8. Brian C. Fairfield, USA</li>
      <li>9. Carmen Gallardo, France</li>
      <li>10. Linda Hartshorn, USA</li>
      <li>11. Harm Koopstra, The Netherlands</li>
      <li>12. Anna-Liisa Salonen, Finland</li>
    </ol>
  </section>
  <div class="abs divider" style="left:558px"></div>
  <ol class="abs list invited-b">
    <li>13. Matthias P. Moser, Germany</li>
    <li>14. Valérie Mercier, France</li>
    <li>15. Kevin A. Morrell, USA</li>
    <li>16. Kazuhiro Nishida, Japan (pending)</li>
    <li>17. Akira Noguchi, Japan</li>
    <li>18. Len Nickerson, USA</li>
    <li>19. M. Samir Oudah, USA</li>
    <li>20. Jorma J. Peltonen, Finland</li>
    <li>21. Elizabeth Radowski, USA</li>
    <li>22. Gabriella Sartori, Italy</li>
    <li>23. Michael Sheldon, USA</li>
    <li>24. Dennis J. Thorne, USA</li>
    <li>25. Jane Tressler, USA</li>
  </ol>

  <div class="abs banner-line"></div>
  <p class="abs forum-name">THE 8th WORLDWIDE FORUM ON<br>TENSION MOLECULES IN LIFE AND HEALING</p>
  <div class="abs tag tag-a"><span>Ivor Bramwell, USA<br>Michael Lindell, USA</span></div>
  <div class="abs tag tag-b"><span>Steve Whitmore<br>Lara Lobato</span></div>
  <h2 class="abs theme">TENSION HANDLING ROUTES AND CIRCUITS</h2>
  <p class="abs dates">August 13-17, 2017</p>

  <div class="abs info venue"><h3>Harborlight Marina Hotel</h3><p>Turku, Finland</p></div>
  <div class="abs info organizer"><h3>ORGANIZER</h3><p>Lea Saarinen<br>Veltrin University<br>Finland</p></div>
  <div class="abs info coorg"><h3>CO-ORGANIZERS</h3><p>Johan Ekholm<br>Veltrin University and Aurajoki University<br>Finland</p></div>
  <div class="abs info coorg2"><h3>Lawrence Holloway</h3><p>Tissue Strain Global Union (TSGU)<br>Eastbrook State University<br>USA</p></div>
  <div class="abs info partner"><h3>Valérie Mercier</h3><p>Université Rive Gauche<br>France</p></div>
  <div class="abs info union"><h3>TISSUE STRAIN GLOBAL<br>UNION (TSGU)</h3><p>VELTRIN UNIVERSITY<br>(VU)</p></div>

  <div class="abs footer-line"></div>
  <div class="abs footer-photo" role="img" aria-label="Close view of rippling sea water in deep teal tones"></div>
  <h2 class="abs contact-box">CONTACT INFORMATION</h2>
  <p class="abs contact contact-1">TSGU &amp; STRAIN AND FOLD LETTERS</p>
  <p class="abs contact contact-2">MANAGING EDITOR GRETA LINDQVIST</p>
  <p class="abs contact contact-3">Dept. of Molecular &amp; Cell Biology<br>Eastbrook State University<br>48 Linden Hill Road Millbrook, CT 06200-1100</p>
  <p class="abs contact contact-4">Phone: (+1) 860 555 0142 &nbsp;|&nbsp; Fax: (+1) 860 555 0187 &nbsp;|&nbsp; Website: www.tissuestrainreplies.org</p>
  <div class="abs uni-mark" aria-hidden="true"></div>
  <p class="abs uni-name">Veltrin<br>University</p>
</main>
</body>
</html>
```